Website front page and logo re-designed (using logo provided)

We are looking for the home page of our new website. It is a website offering a space for clients to ask professionals questions. The website should be similar in design to www.brimtolo.com however it is clear it should be a different look. It should be modern, simple to use, a clear navigation bar at the top and bottom.

Logo should be similar to the one attached, but more professional and modern. Logo should be clearly incorporated into website. Design should focus on our website colours as in the logo.

Logo Text

Kelvora - Clarity at every turn!

Number of Pages Required

1 page

Font styles to use
Sans Serif

```html
<!DOCTYPE html>
<html lang="en">
<head>
<meta charset="utf-8">
<title>Kelvora - Clarity at every turn!</title>
<link href="https://fonts.googleapis.com/css2?family=Lato:ital,wght@0,400;0,700;1,400;1,700&family=Raleway:wght@400;500;600&display=swap" rel="stylesheet">
<style>
:root{
  --green:#2f9417;
  --green-dark:#24760f;
  --red:#d52b2b;
  --red-dark:#b71f1f;
  --ink:#222;
  --muted:#666;
  --line:#d4d4d4;
  --footer:#333;
  --footer-side:#3d3d3d;
  --footer-base:#262626;
  --star:#e8b400;
}
*{box-sizing:border-box;margin:0;padding:0}
html,body{width:1200px;height:2917px;overflow:hidden}
body{position:relative;background:#fff;font-family:'Lato',sans-serif;color:var(--ink)}
.abs{position:absolute}
.heading{font-family:'Raleway',sans-serif;font-weight:400}

/* header */
.site-header{position:absolute;left:0;top:0;width:1200px;height:88px;background:#fff}
.brand{left:58px;top:12px}
.brand-name{font-family:'Lato',sans-serif;font-weight:700;font-size:38px;line-height:40px;color:var(--green);letter-spacing:1px}
.brand-tag{font-size:17px;color:var(--ink);margin-top:1px;padding-left:16px}
.guarantee{left:700px;top:23px;width:214px;height:45px;border:1px solid #ccc;border-radius:4px;display:flex;align-items:center;padding-left:12px;gap:6px}
.guarantee b{font-size:28px;color:var(--green);font-weight:700}
.guarantee span{font-size:11px;color:var(--green);line-height:12px}
.nav-btn{top:25px;height:40px;border:1px solid #ccc;border-radius:4px;font-size:14px;color:var(--red);display:flex;align-items:center;justify-content:center}

/* hero */
.hero{left:0;top:88px;width:1200px;height:470px;background:linear-gradient(180deg,#5a2e1f 0%,#6a3826 45%,#4b2518 100%)}
.hero-figure{left:770px;top:0;width:430px;height:470px;background:linear-gradient(90deg,rgba(30,20,18,0) 0%,#2a1d1a 35%,#1f1716 100%)}
.hero-title{left:58px;top:90px;color:#fff;font-weight:700;font-style:italic;font-size:38px;line-height:50px;text-shadow:0 2px 4px rgba(0,0,0,.4)}
.hero-sub{left:58px;top:198px;color:#fff;font-family:'Raleway',sans-serif;font-weight:500;font-size:23px}
.ask-box{left:52px;top:287px;width:934px;height:121px;background:var(--red)}
.tabs{display:flex;height:38px}
.tabs span{color:#fff;font-size:16px;line-height:38px;padding:0 26px}
.tabs span.on{background:var(--red-dark)}
.ask-input{position:absolute;left:36px;top:49px;width:880px;height:38px;background:#fff;font-size:14px;color:#777;line-height:38px;padding-left:14px}
.ask-note{left:470px;top:428px;color:#fff;font-size:13px;font-style:italic;font-weight:700}
.ask-btn{left:811px;top:412px;width:175px;height:41px;background:var(--green);color:#fff;font-weight:700;font-size:16px;display:flex;align-items:center;justify-content:center}

/* experts */
.section-title{width:1200px;left:0;text-align:center}
.expert{top:675px;width:284px;height:150px;border:1px solid var(--line);background:#fff}
.expert .photo{position:absolute;left:0;top:0;width:140px;height:148px;background:linear-gradient(160deg,#c9ccd2,#8b8f98)}
.expert .info{position:absolute;left:156px;top:12px}
.stars{color:var(--red);font-size:13px;letter-spacing:3px}
.expert h3{font-family:'Raleway',sans-serif;font-weight:400;font-size:22px;margin-top:6px}
.expert .role{font-style:italic;font-size:13px;color:var(--muted)}
.expert .count{font-style:italic;font-size:13px;color:var(--muted);margin-top:20px;line-height:16px}
.expert .count b{color:var(--green)}
.chev{width:38px;height:70px}

/* why */
.why{left:0;top:879px;width:1200px;height:486px;background:var(--green);color:#fff}
.feature{top:1025px;width:230px;text-align:center}
.feature svg{display:block;margin:0 auto 16px}
.feature h4{font-family:'Raleway',sans-serif;font-weight:400;font-size:23px;margin-bottom:12px}
.feature p{font-size:13px;line-height:23px}
.ghost-btn{border:1.5px solid #fff;border-radius:6px;color:#fff;font-family:'Raleway',sans-serif;font-size:23px;display:flex;align-items:center;justify-content:center}

/* questions */
.join{left:0;top:1365px;width:1200px;height:611px;background:linear-gradient(180deg,#5b5b5b 0%,#3b3b3b 55%,#2c2c2c 100%);color:#fff}
.q-table{left:52px;top:1572px;width:1096px}
.q-head{display:flex;height:40px;align-items:center;font-size:17px;border-bottom:1.5px solid #e6e6e6;padding-left:4px}
.q-row{display:flex;height:41px;align-items:center;font-size:14px;font-style:italic;border-bottom:1px solid rgba(255,255,255,.25);padding-left:12px}
.q-row.hot{background:var(--red)}
.q-row .q{width:825px}
.q-head .q{width:837px}
.q-row .r,.q-head .r{width:146px;color:var(--star);letter-spacing:4px;font-size:12px;font-style:normal}
.q-head .r{color:#fff;letter-spacing:0;font-size:17px}
.q-row .d{font-size:12px}

/* testimonials */
.quote-mark{left:499px;top:2137px;width:110px;height:110px;border-radius:50%;background:#333}
.quote-face{left:594px;top:2137px;width:110px;height:110px;border-radius:50%;background:linear-gradient(160deg,#e6e6e6,#9a9a9a);border:4px solid #fff;box-shadow:0 0 0 1px #ddd}
.quote-text{left:160px;top:2285px;width:880px;text-align:center;font-style:italic;font-size:23px;line-height:35px;color:#555}
.quote-name{left:0;top:2374px;width:1200px;text-align:center;color:var(--green);font-family:'Raleway',sans-serif;font-size:25px}
.red-btn{left:469px;top:2464px;width:260px;height:42px;border:1.5px solid var(--red);border-radius:4px;color:var(--red);font-size:17px;display:flex;align-items:center;justify-content:center}

/* footer */
.footer{left:0;top:2563px;width:1200px;height:308px;background:var(--footer);color:#fff}
.footer-side{left:0;top:2563px;width:370px;height:308px;background:var(--footer-side)}
.f-head{font-family:'Raleway',sans-serif;font-size:16px;letter-spacing:.5px;color:#fff}
.f-links{font-size:13px;line-height:24px;color:#e8e8e8;list-style:none}
.article{left:52px;width:300px;height:70px}
.article .thumb{position:absolute;left:0;top:0;width:113px;height:70px;background:linear-gradient(135deg,#b7c4d3,#6c7d91)}
.article .date{position:absolute;left:133px;top:2px;font-size:11px;color:#888}
.article .txt{position:absolute;left:133px;top:24px;font-size:13px;line-height:20px;color:#fff}
.social{top:2812px;width:36px;height:36px;border-radius:50%}
.badge{top:2803px;height:48px;border-radius:4px}
.copyright{left:0;top:2871px;width:1200px;height:46px;background:var(--footer-base);color:#ddd;font-size:13px;display:flex;align-items:center;justify-content:center}
</style>
</head>
<body>

<header class="site-header">
  <div class="abs brand">
    <div class="brand-name">Kelvora</div>
    <div class="brand-tag">Clarity at every turn!</div>
  </div>
  <div class="abs guarantee">
    <svg width="26" height="26" viewBox="0 0 26 26"><path d="M4 14l6 6L22 6" fill="none" stroke="#2f9417" stroke-width="4"/></svg>
    <b>100%</b><span>Satisfaction<br>Guaranteed</span>
  </div>
  <div class="abs nav-btn" style="left:930px;width:62px">LOGIN</div>
  <div class="abs nav-btn" style="left:1008px;width:140px">HOW IT WORKS</div>
</header>

<section class="abs hero" role="img" aria-label="Background of leather-bound law books on shelves">
  <div class="abs hero-figure" role="img" aria-label="Barrister in wig and gown holding a rolled document"></div>
</section>
<h1 class="abs hero-title">Ask Your Question,<br>Get An Answer ASAP</h1>
<p class="abs hero-sub">A New Question Is Answered Every 9 Seconds</p>
<div class="abs ask-box">
  <div class="tabs">
    <span class="on">Lawyers</span><span>Mechanics</span><span>Doctors &amp; Nurses</span><span>Vets</span><span>Computer &amp; Education</span><span>MoreCategories..</span>
  </div>
  <div class="ask-input">Choose Your Expert And Type Your Question Here...</div>
</div>
<p class="abs ask-note">Get Answer From More Then 54 Experts Online Now</p>
<div class="abs ask-btn">GET AN ANSWER</div>

<h2 class="abs section-title heading" style="top:595px;font-size:40px">Our Experts</h2>
<svg class="abs chev" style="left:70px;top:714px" viewBox="0 0 38 70"><path d="M34 2L4 35l30 33" fill="none" stroke="#555" stroke-width="2"/></svg>
<svg class="abs chev" style="left:1092px;top:714px" viewBox="0 0 38 70"><path d="M4 2l30 33L4 68" fill="none" stroke="#555" stroke-width="2"/></svg>
<div class="abs expert" style="left:128px">
  <div class="photo" role="img" aria-label="Portrait of a smiling woman in a business suit"></div>
  <div class="info"><div class="stars">★★★★★</div><h3>Tina</h3><div class="role">Lawyer</div><div class="count"><b>4566</b> Satisfied<br>Customers</div></div>
</div>
<div class="abs expert" style="left:457px">
  <div class="photo" role="img" aria-label="Portrait of a smiling man in a blue shirt"></div>
  <div class="info"><div class="stars">★★★★★</div><h3>Ely</h3><div class="role">Medical Councelor</div><div class="count"><b>4566</b> Satisfied<br>Customers</div></div>
</div>
<div class="abs expert" style="left:786px">
  <div class="photo" role="img" aria-label="Portrait of a smiling man in a jacket"></div>
  <div class="info"><div class="stars">★★★★★</div><h3>Dr. Chip</h3><div class="role">Doctor (MD)</div><div class="count"><b>4566</b> Satisfied<br>Customers</div></div>
</div>

<section class="abs why">
  <h2 class="abs section-title heading" style="top:45px;font-size:40px;color:#fff">Why Ask A Question On Kelvora?</h2>
</section>
<div class="abs feature" style="left:46px;color:#fff">
  <svg width="60" height="70" viewBox="0 0 60 70" fill="#1d5e0d"><circle cx="26" cy="14" r="12" fill="none" stroke="#1d5e0d" stroke-width="3"/><rect x="21" y="12" width="10" height="34" rx="5"/><rect x="14" y="34" width="34" height="32" rx="8"/></svg>
  <h4>Convenience</h4><p>Enjoy a fast, easy way to ask<br>Experts anywhere you're online</p>
</div>
<div class="abs feature" style="left:258px;color:#fff">
  <svg width="110" height="70" viewBox="0 0 110 70" fill="#1d5e0d"><circle cx="22" cy="32" r="10"/><path d="M4 66c0-16 36-16 36 0z"/><circle cx="88" cy="32" r="10"/><path d="M70 66c0-16 36-16 36 0z"/><path d="M38 18q17-16 34 0" fill="none" stroke="#1d5e0d" stroke-width="4"/><path d="M72 44q-17 16-34 0" fill="none" stroke="#1d5e0d" stroke-width="4"/></svg>
  <h4>One On One</h4><p>Ask Experts who follow up<br>with you until you're done</p>
</div>
<div class="abs feature" style="left:484px;color:#fff">
  <svg width="70" height="70" viewBox="0 0 70 70"><circle cx="35" cy="35" r="30" fill="none" stroke="#1d5e0d" stroke-width="5"/><text x="35" y="43" text-anchor="middle" font-family="Lato,sans-serif" font-weight="700" font-size="22" fill="#1d5e0d">24h</text></svg>
  <h4>24/7 Availability</h4><p>Ask a question at night or on<br>weekends and get it answered</p>
</div>
<div class="abs feature" style="left:702px;color:#fff">
  <svg width="80" height="70" viewBox="0 0 80 70" fill="#1d5e0d"><circle cx="28" cy="22" r="11"/><path d="M6 68c0-26 44-26 44 0z"/><circle cx="58" cy="20" r="16" fill="none" stroke="#1d5e0d" stroke-width="3"/><path d="M42 20h32M58 4v32" stroke="#1d5e0d" stroke-width="2"/></svg>
  <h4>Broad Expertise</h4><p>Over 150 types of Experts<br>cover any topic and question!</p>
</div>
<div class="abs feature" style="left:922px;color:#fff">
  <svg width="60" height="70" viewBox="0 0 60 70" fill="#1d5e0d"><rect x="4" y="32" width="12" height="32"/><path d="M20 32l12-26c6 0 8 4 7 10l-3 12h16c4 0 6 4 5 7l-5 24c-1 3-3 5-6 5H20z"/></svg>
  <h4>100% Satisfaction</h4><p>Millions have asked questions<br>with guaranteed satisfaction</p>
</div>
<div class="abs ghost-btn" style="left:412px;top:1249px;width:376px;height:50px">Ask &amp; Get It Answered Now!</div>

<section class="abs join" role="img" aria-label="Background of hands typing on a keyboard in grey tones"></section>
<h2 class="abs section-title heading" style="top:1420px;font-size:44px;color:#fff">Join The 9 Million People</h2>
<h3 class="abs section-title heading" style="top:1488px;font-size:36px;color:#fff">Who Found A Smarter Way To Get Expert Help</h3>
<div class="abs q-table" style="color:#fff">
  <div class="q-head"><span class="q">Recently Answered Questions</span><span class="r">Rating</span><span>Date</span></div>
  <div class="q-row hot"><span class="q">Vantaro Quiet Series 4 Dishwasher About 10 Years Old</span><span class="r">★★★★<span style="color:#ddd">★</span></span><span class="d">2 hrs ago</span></div>
  <div class="q-row"><span class="q">i was criticized and derided by a plaintiff's attorney in an</span><span class="r">★★★★<span style="color:#ddd">★</span></span><span class="d">2 hrs ago</span></div>
  <div class="q-row"><span class="q">I had a tenant who I evicted last August, who left many personal</span><span class="r">★★★★<span style="color:#ddd">★</span></span><span class="d">2 hrs ago</span></div>
  <div class="q-row"><span class="q">My keyboard is locked on my Norvik keyboard</span><span class="r">★★★★<span style="color:#ddd">★</span></span><span class="d">2 hrs ago</span></div>
  <div class="q-row"><span class="q">Vantaro Quiet Series 4 Dishwasher About 10 Years Old</span><span class="r">★★★★<span style="color:#ddd">★</span></span><span class="d">2 hrs ago</span></div>
</div>
<div class="abs ghost-btn" style="left:459px;top:1863px;width:282px;height:51px;background:rgba(0,0,0,.25)">View All Questions</div>

<h2 class="abs section-title heading" style="top:2040px;font-size:46px">Customers Love Kelvora</h2>
<div class="abs quote-mark"><svg width="110" height="110" viewBox="0 0 110 110"><text x="55" y="92" text-anchor="middle" font-family="Georgia,serif" font-weight="700" font-size="96" fill="#fff">“</text></svg></div>
<div class="abs quote-face" role="img" aria-label="Portrait of a grey-haired customer"></div>
<svg class="abs chev" style="left:70px;top:2241px" viewBox="0 0 38 70"><path d="M34 2L4 35l30 33" fill="none" stroke="#555" stroke-width="2"/></svg>
<svg class="abs chev" style="left:1092px;top:2241px" viewBox="0 0 38 70"><path d="M4 2l30 33L4 68" fill="none" stroke="#555" stroke-width="2"/></svg>
<p class="abs quote-text">The service technician was dead on the money with his fix and provided me with a link to an online video that showed exactly how to replace the part.</p>
<p class="abs quote-name">Dale Minter, Ashford, USA</p>
<div class="abs red-btn">View All Client Reviews</div>

<footer>
  <div class="abs footer"></div>
  <div class="abs footer-side"></div>
  <div class="abs f-head" style="left:52px;top:2597px">FREE EXPERT TIPS &amp; ARTICLES</div>
  <div class="abs article" style="top:2641px"><div class="thumb" role="img" aria-label="Business people meeting"></div><div class="date">03 JAN, 2016</div><div class="txt">Lorem ipsum dolor sit amet<br>ipsum dolor sit amet</div></div>
  <div class="abs article" style="top:2729px"><div class="thumb" role="img" aria-label="Business people meeting"></div><div class="date">03 JAN, 2016</div><div class="txt">Lorem ipsum dolor sit amet<br>ipsum dolor sit amet</div></div>
  <div class="abs" style="left:52px;top:2818px;font-size:13px;color:#ccc">VIEW ALL ARTICLES</div>

  <div class="abs f-head" style="left:408px;top:2597px">QUICK LINKS</div>
  <ul class="abs f-links" style="left:412px;top:2633px"><li>About Brimtolo</li><li>How It Works</li><li>Press Room</li></ul>
  <div class="abs f-head" style="left:574px;top:2597px">USING KELVORA</div>
  <ul class="abs f-links" style="left:574px;top:2633px"><li>Browse Categories ›</li><li>Meet the Experts</li><li>Other Countries ›</li></ul>
  <div class="abs f-head" style="left:801px;top:2597px">CUSTOMER CARE</div>
  <ul class="abs f-links" style="left:804px;top:2633px"><li>Contact Us</li><li>Help FAQs</li><li>The Brimtolo Promise</li><li>Login</li><li>Register</li></ul>
  <div class="abs f-head" style="left:1006px;top:2597px">JOIN US</div>
  <ul class="abs f-links" style="left:1006px;top:2633px"><li>Careers</li><li>Become an Expert</li><li>Become an Affiliate</li><li>Refer an Expert</li></ul>

  <div class="abs f-head" style="left:408px;top:2776px">SOCIAL MEDIA</div>
  <div class="abs social" style="left:410px;background:#2f6fae"></div>
  <div class="abs social" style="left:462px;background:#2aa6d8"></div>
  <div class="abs social" style="left:514px;background:#1a7fb5"></div>
  <div class="abs social" style="left:566px;background:#d0473a"></div>

  <div class="abs badge" style="left:745px;width:110px;background:#f2f2f2"></div>
  <div class="abs badge" style="left:870px;width:127px;background:#2c5e8f"></div>
  <div class="abs badge" style="left:1015px;width:128px;background:#f2f2f2"></div>

  <div class="abs copyright">Copyright 2016 Kelvora &nbsp;|&nbsp; All Rights Reserved.</div>
</footer>

</body>
</html>
```